TotsyPlum Business needs a Box Design

We need a box design for a new product Teething Mittens. Please check our file for a demo and Layout, Box mockup, Logo Vector
https://files.sharevault-example.com/folders/8kQzLmW3pXrT7nVb2YcHd4JfGs9Ne6Ua

Target Market(s)

A parent have baby 6 - 12 month

Industry/Entity Type

Baby

Font styles to use
Decorative
Script

Requirements
Must have
• Our logo in a Box and follow our guide
Nice to have
• Cute design

```html
<!DOCTYPE html>
<html lang="en">
<head>
<meta charset="utf-8">
<title>TotsyPlum Baby Mitten Box</title>
<link rel="stylesheet" href="https://fonts.googleapis.com/css2?family=Ultra&family=Quicksand:wght@400;500&family=Oswald:wght@300;400&display=swap">
<style>
  :root{
    --bg-top:#fdfbf1;
    --bg-bottom:#f8e48c;
    --gold:#e0b462;
    --pink:#f8d3d8;
    --pink-deep:#f0a9b4;
    --coral:#ef5b6c;
    --teal:#7cc2b4;
    --mint:#d5eaeb;
    --sky:#cfe7ee;
    --butter:#f6e69a;
    --paper:#ffffff;
    --ink:#55505a;
    --badge:#2b2a2c;
    --glass-a:#5c5c5c;
    --glass-b:#c8c8c8;
  }
  *{box-sizing:border-box;margin:0;padding:0}
  html,body{width:1200px;height:1200px;overflow:hidden}
  body{background:linear-gradient(180deg,var(--bg-top) 0%,#fbf1c2 45%,var(--bg-bottom) 100%);font-family:'Quicksand',sans-serif;position:relative}

  .brand-lockup{position:absolute;top:150px;left:0;width:1200px;text-align:center}
  .brand-name{font-family:'Quicksand',sans-serif;font-weight:400;font-size:58px;color:var(--gold);letter-spacing:1px}
  .brand-mark-dot{display:inline-block;width:26px;height:26px;border-radius:50%;background:var(--gold);vertical-align:middle;margin-right:14px}

  .dieline{position:absolute;top:300px;left:165px;width:870px;height:840px}
  .panel{position:absolute;top:0}
  .panel-front{left:0;width:360px}
  .panel-side{left:380px;width:110px}
  .panel-back{left:510px;width:360px}

  .hang-tab{height:120px;background:var(--pink);position:relative;border-radius:2px 2px 0 0}
  .hang-hole{position:absolute;left:50%;top:46px;width:96px;height:32px;margin-left:-48px;background:var(--bg-top);border-radius:16px}
  .hang-hole::before{content:"";position:absolute;left:36px;top:-12px;width:24px;height:20px;border-radius:12px 12px 0 0;background:var(--bg-top)}
  .tab-spacer{height:120px}

  .box-face{position:relative;height:560px;background:var(--paper);overflow:hidden;box-shadow:0 18px 30px rgba(170,140,40,.25)}
  .top-strip{height:40px;background:var(--pink)}
  .face-art{position:absolute;inset:0;width:100%;height:100%}

  .face-logo{position:absolute;left:0;width:100%;text-align:center;font-family:'Quicksand',sans-serif;font-weight:400;color:var(--gold)}
  .front-logo{top:92px;font-size:24px}
  .window{position:absolute;left:40px;top:145px;width:280px;height:280px;border-radius:26px;background:linear-gradient(135deg,var(--glass-a) 0%,#8a8a8a 40%,var(--glass-b) 55%,#7a7a7a 75%,var(--glass-a) 100%)}
  .product-title{position:absolute;left:0;width:100%;bottom:32px;text-align:center;font-family:'Ultra',serif;font-size:38px;letter-spacing:1px}
  .word-baby{color:var(--coral)}
  .word-mitten{color:var(--teal)}

  .side-title{position:absolute;left:50%;top:290px;transform:translate(-50%,-50%) rotate(90deg);white-space:nowrap;font-family:'Ultra',serif;font-size:32px}
  .side-logo{position:absolute;left:50%;bottom:60px;transform:translateX(-50%) rotate(-60deg);font-size:14px;color:var(--gold);white-space:nowrap}

  .back-logo{top:72px;font-size:18px}
  .back-copy{position:absolute;left:26px;top:118px;width:200px;font-family:'Oswald',sans-serif;font-weight:300;font-size:9.5px;line-height:1.45;color:var(--ink)}
  .back-copy h3{font-family:'Oswald',sans-serif;font-weight:400;font-size:12px;color:var(--coral);letter-spacing:.5px;margin:8px 0 3px}
  .back-copy ul{list-style:none}
  .back-copy li::before{content:"- "}
  .badge{position:absolute;right:42px;width:44px;height:44px;border-radius:50%;background:var(--badge);box-shadow:0 0 0 3px #caa257}
  .badge-best{top:170px}
  .badge-premium{top:232px}
  .pattern-swatch{position:absolute;left:70px;top:390px;width:90px;height:90px;border-radius:50%;background:radial-gradient(circle,#e8e4e6 0%,#d6cfd2 60%,#c3c5cc 100%)}
  .pattern-label{position:absolute;font-family:'Oswald',sans-serif;font-weight:300;font-size:9px;color:var(--coral);letter-spacing:.5px}
  .label-a{left:170px;top:380px}
  .label-b{left:60px;top:490px}
  .label-c{left:165px;top:495px}
  .back-corner-logo{position:absolute;right:20px;bottom:40px;font-size:13px;color:var(--gold);transform:rotate(-25deg)}
</style>
</head>
<body>

  <header class="brand-lockup">
    <span class="brand-mark-dot"></span><span class="brand-name">TotsyPlum</span>
  </header>

  <main class="dieline">

    <section class="panel panel-front">
      <div class="hang-tab"><span class="hang-hole"></span></div>
      <div class="box-face">
        <svg class="face-art" viewBox="0 0 360 560" preserveAspectRatio="none" aria-hidden="true">
          <rect y="0" width="360" height="40" fill="var(--pink)"/>
          <circle cx="22" cy="92" r="7" fill="var(--pink)"/>
          <circle cx="44" cy="150" r="28" fill="var(--sky)"/>
          <path d="M262 100 q30 -28 62 -6 q18 26 -20 40 q-34 8 -42 -34z" fill="var(--pink)"/>
          <path d="M244 104 q22 -18 36 4 q6 26 -18 28 q-22 -6 -18 -32z" fill="var(--butter)"/>
          <circle cx="340" cy="320" r="6" fill="var(--sky)"/>
          <ellipse cx="348" cy="380" rx="12" ry="34" fill="var(--butter)"/>
          <path d="M0 470 q90 -40 180 -10 q100 30 180 -20 L360 560 L0 560z" fill="var(--mint)"/>
          <ellipse cx="40" cy="470" rx="26" ry="18" fill="var(--butter)"/>
        </svg>
        <div class="face-logo front-logo">TotsyPlum</div>
        <div class="window" role="img" aria-label="Clear window showing the teething mittens inside"></div>
        <div class="product-title"><span class="word-baby">BABY</span> <span class="word-mitten">MITTEN</span></div>
      </div>
    </section>

    <section class="panel panel-side">
      <div class="tab-spacer"></div>
      <div class="box-face">
        <svg class="face-art" viewBox="0 0 110 560" preserveAspectRatio="none" aria-hidden="true">
          <rect y="0" width="110" height="40" fill="var(--pink)"/>
          <ellipse cx="30" cy="100" rx="8" ry="26" fill="var(--sky)"/>
          <circle cx="60" cy="160" r="16" fill="var(--pink)"/>
          <circle cx="90" cy="70" r="6" fill="var(--butter)"/>
          <circle cx="20" cy="400" r="5" fill="var(--pink)"/>
          <path d="M0 500 q55 -20 110 10 L110 560 L0 560z" fill="var(--mint)"/>
        </svg>
        <div class="side-title"><span class="word-baby">BABY</span> <span class="word-mitten">MITTEN</span></div>
        <div class="side-logo">TotsyPlum</div>
      </div>
    </section>

    <section class="panel panel-back">
      <div class="hang-tab"><span class="hang-hole"></span></div>
      <div class="box-face">
        <svg class="face-art" viewBox="0 0 360 560" preserveAspectRatio="none" aria-hidden="true">
          <rect y="0" width="360" height="40" fill="var(--pink)"/>
          <path d="M40 470 q60 -50 140 -20 q70 20 110 -10 L300 560 L30 560z" fill="var(--mint)"/>
          <ellipse cx="300" cy="440" rx="18" ry="10" fill="var(--pink)"/>
          <ellipse cx="316" cy="456" rx="10" ry="6" fill="var(--butter)"/>
        </svg>
        <div class="face-logo back-logo">TotsyPlum</div>
        <div class="back-copy">
          <h3>INSTRUCTIONS FOR USE</h3>
          <p>Slip the mitten over baby's hand and fasten the soft strap. Check the fit often. Chill in the fridge for extra soothing relief during teething.</p>
          <h3>WASH INSTRUCTIONS</h3>
          <p>Hand wash in warm soapy water and lay flat to dry.</p>
          <h3>WARNING</h3>
          <ul>
            <li>Always supervise baby while in use.</li>
            <li>Check for wear before each use.</li>
            <li>Discard if torn or damaged.</li>
            <li>Do not heat in microwave.</li>
            <li>Keep away from open flame.</li>
            <li>Not a substitute for feeding.</li>
          </ul>
        </div>
        <div class="badge badge-best"></div>
        <div class="badge badge-premium"></div>
        <div class="pattern-swatch" role="img" aria-label="Round swatch of the mitten fabric print with little animals"></div>
        <span class="pattern-label label-a">LOREM IPSUM</span>
        <span class="pattern-label label-b">LOREM IPSUM</span>
        <span class="pattern-label label-c">LOREM IPSUM</span>
        <div class="back-corner-logo">TotsyPlum</div>
      </div>
    </section>

  </main>
</body>
</html>
```